New Peanut Butter Brand Needs Product Label

We need a packaging label for a new to market peanut butter product based in the UK. The range of peanut butters will include a range of great flavours. We have been looking at labels to give inspiration and we are liking the less complicated designs that are on a white background (Sample designs are attached).

The company is called 'Breezy Acorn Company' The name could be used in full or shortened to 'Breezy Acorn Co'

The design should be a little fun and cool (not in a childish way), using bright colours and a mixture of fonts would be fine (as long as the text is easy to read)

For the purposes of this design brief text that should be added to the front of the design is

Brand name (As above)
Sea Salt (The flavour of this product)
Chunky (Peanut butter is chunky or smooth right !!)

Allowance should be given for the ingredients panel and standard information used on a food product.

Key phrases that could be used in the design are below

Great source of protein
Heart Healthy
Packed with nutrients

The food container will be a plastic pot and so the labels are slightly curved. I have attached a picture of a similar pot and a label outline an sizing which should be of help.

```html
<!DOCTYPE html>
<html lang="en">
<head>
<meta charset="utf-8">
<title>Breezy Acorn Co – Sea Salt Chunky Peanut Butter Label</title>
<link rel="stylesheet" href="https://fonts.googleapis.com/css2?family=Chewy&family=Kalam:wght@400&family=Varela+Round&family=Roboto:wght@400;700&display=swap">
<style>
  :root {
    --backdrop: #e8ae56;
    --label: #ffffff;
    --brand-orange: #e8562a;
    --ribbon-yellow: #f7c21a;
    --frame-brown: #7a2b1c;
    --text-brown: #6b2a1a;
    --sea-blue: #1a95d8;
    --sea-light: #6ec3ee;
    --bullet-orange: #eea93a;
  }
  * { margin: 0; padding: 0; box-sizing: border-box; }
  html, body { width: 1200px; height: 1000px; overflow: hidden; }
  body { background: var(--backdrop); position: relative; font-family: "Roboto", sans-serif; }

  .label {
    position: absolute; left: 100px; top: 176px; width: 994px; height: 630px;
    background: var(--label);
    box-shadow: 6px 8px 14px rgba(90, 50, 10, 0.35);
  }
  .front-frame {
    position: absolute; left: 24px; top: 24px; width: 588px; height: 590px;
    border: 2px solid var(--frame-brown); border-radius: 18px;
  }
  .brand-name {
    position: absolute; left: 24px; top: 88px; width: 588px;
    text-align: center;
    font-family: "Roboto", sans-serif; font-weight: 700; font-size: 58px; line-height: 64px;
    color: var(--brand-orange);
  }
  .ribbon { position: absolute; left: 158px; top: 166px; width: 316px; height: 60px; }
  .ribbon text {
    font-family: "Roboto", sans-serif; font-weight: 700; font-size: 27px; fill: #fff;
  }
  .flavour { position: absolute; left: 90px; top: 246px; color: var(--sea-blue); }
  .flavour-name { font-family: "Varela Round", sans-serif; font-size: 40px; line-height: 44px; }
  .flavour-word {
    font-family: "Varela Round", sans-serif; font-size: 26px; line-height: 26px;
    color: var(--sea-light); margin-left: 62px;
  }
  .texture {
    position: absolute; left: 372px; top: 240px;
    font-family: "Chewy", "Kalam", cursive; font-size: 50px; line-height: 56px; color: var(--text-brown);
    transform: rotate(9deg); transform-origin: left center;
  }
  .product-photo {
    position: absolute; left: 75px; top: 320px; width: 460px; height: 275px;
    border-radius: 40px;
    background: radial-gradient(ellipse at 55% 50%, #d9a160 0%, #8a5530 45%, #f3f0ea 80%, #ffffff 100%);
  }
  .benefits { position: absolute; left: 652px; top: 42px; list-style: none; }
  .benefits li {
    display: flex; align-items: center; height: 42px;
    font-family: "Kalam", cursive; font-size: 26px; color: var(--text-brown);
  }
  .benefit-mark {
    width: 34px; height: 22px; border-radius: 50%; background: var(--bullet-orange);
    margin-right: 16px; transform: rotate(-25deg);
  }
  .ingredients {
    position: absolute; left: 658px; top: 209px; width: 309px; height: 395px;
    border: 2px solid var(--frame-brown);
  }
  .ingredients h2 {
    font-family: "Roboto", sans-serif; font-weight: 400; font-size: 20px;
    color: var(--text-brown); text-align: center; margin-top: 20px; letter-spacing: 0.5px;
  }
</style>
</head>
<body>
  <main class="label">
    <section class="front-panel">
      <div class="front-frame"></div>

      <h1 class="brand-name">Breezy Acorn Co</h1>

      <svg class="ribbon" viewBox="0 0 316 60">
        <polygon points="0,6 316,0 300,30 316,56 0,60 12,33" fill="var(--ribbon-yellow)"/>
        <text x="158" y="40" text-anchor="middle">PEANUT BUTTER</text>
      </svg>

      <div class="flavour">
        <div class="flavour-name">Sea Salt</div>
        <div class="flavour-word">flavour</div>
      </div>

      <div class="texture">Chunky</div>

      <div class="product-photo" role="img" aria-label="Photo of toast spread with peanut butter, an open jar, a knife, whole peanuts and a pile of sea salt"></div>
    </section>

    <section class="back-panel">
      <ul class="benefits">
        <li><span class="benefit-mark"></span>Great source of protein</li>
        <li><span class="benefit-mark"></span>Heart Healthy</li>
        <li><span class="benefit-mark"></span>Packed with nutrients</li>
      </ul>
      <div class="ingredients">
        <h2>INGREDIENTS</h2>
      </div>
    </section>
  </main>
</body>
</html>
```